Plumbing business looking for a website update / to stand out

Looking to update the website with WordPress so looking for a WordPress template customised to our needs. The current website is http://www.corwinhaleplumbing.com.au/ and would like to keep the colour scheme of the green and grey. Like the idea of have menu across the top with drop down menus once mouse is over them.

Looking to stand out and look professional when compared to the competition
http://www.redgroveplumbing.net.au/
http://www.tovisplumbing.com.au/

```html
<!DOCTYPE html>
<html lang="en">
<head>
<meta charset="utf-8">
<title>Corwin Hale Plumbing</title>
<link href="https://fonts.googleapis.com/css2?family=Roboto:wght@300;400;500&display=swap" rel="stylesheet">
<style>
:root{
  --green:#6cbb3c;
  --green-dark:#4f9a27;
  --grey-text:#8a8a8a;
  --heading:#444;
  --footer:#5b5c5e;
  --footer-bottom:#404144;
  --nav-active:#2f2f2f;
}
*{margin:0;padding:0;box-sizing:border-box}
html,body{width:814px;height:1200px;overflow:hidden;background:#fff;font-family:'Roboto',Arial,sans-serif}
.page{position:relative;width:814px;height:1200px}
.brand{position:absolute;left:96px;top:18px;display:flex;align-items:center;gap:8px}
.brand-dot{width:34px;height:34px;border-radius:50%;background:var(--green)}
.brand-name{font-size:17px;font-weight:500;color:#555;line-height:1}
.brand-tag{font-size:8px;color:#666;margin-top:4px}
.social{display:flex;gap:4px}
.social span{width:22px;height:22px;border-radius:50%;background:#6d6e70}
.social span:first-child{background:var(--green)}
.header-social{position:absolute;right:82px;top:25px}
.header-phone{position:absolute;right:82px;top:58px;font-size:13px;font-weight:300;color:#555;display:flex;align-items:center;gap:4px}
.header-phone b{font-weight:300;color:var(--green)}
.nav{position:absolute;top:94px;left:0;width:814px;height:36px;background:linear-gradient(#79c544,#5aa82c);display:flex;padding-left:150px}
.nav a{color:#fff;text-decoration:none;font-size:13px;font-weight:300;padding:0 26px;line-height:36px;border-right:1px solid rgba(0,0,0,.15)}
.nav a.active{background:var(--nav-active);padding:0 24px}
.nav a:last-child{border:none}
.hero{position:absolute;top:130px;left:0;width:814px;height:277px;background:linear-gradient(135deg,#8f8d80,#c9c6b8 45%,#a39a7e 75%,#6f6a57)}
.dots{position:absolute;top:389px;left:368px;display:flex;gap:6px}
.dots i{width:7px;height:7px;border-radius:50%;background:#bbb}
.dots i:first-child{background:var(--green)}
.card{position:absolute;top:436px;width:193px}
.card h3{font-size:12.5px;font-weight:400;color:var(--heading);margin-bottom:10px}
.card .photo{height:106px;border:1px solid #ddd}
.card p{margin-top:20px;font-size:7.3px;line-height:12px;color:var(--grey-text)}
.btn{display:inline-block;margin-top:22px;background:var(--green);color:#fff;font-size:9px;padding:6px 10px}
.welcome{position:absolute;left:91px;top:720px;width:410px}
.welcome h2,.member h2{font-size:20px;font-weight:300;color:var(--heading);margin-bottom:34px}
.welcome p{font-size:8.6px;line-height:12px;color:var(--grey-text);margin-bottom:12px}
.divider{position:absolute;left:526px;top:718px;width:1px;height:258px;background:#e6e6e6}
.member{position:absolute;left:551px;top:720px}
.badge{width:175px;height:200px;display:block}
.footer{position:absolute;top:987px;left:0;width:814px;height:175px;background:var(--footer)}
.footer h4{font-size:16px;font-weight:400;color:#fff;margin-bottom:16px}
.col{position:absolute;top:10px}
.menu a{display:block;color:#ddd;font-size:8.6px;text-decoration:none;margin-bottom:11px}
.menu a.active{color:var(--green)}
.contact-line{font-size:8.6px;color:#ddd;margin-bottom:11px;display:flex;gap:6px;align-items:flex-start}
.contact-line em{font-style:normal;color:var(--green)}
.contact-line svg{flex:none}
.field{width:153px;height:20px;border:1px solid #888;background:#4a4b4d;color:#bbb;font-size:8.6px;padding:4px 5px;margin-bottom:6px}
.field.first{border-color:var(--green)}
.field.area{height:47px}
.submit{margin-left:80px;width:73px;height:23px;background:var(--green);color:#fff;font-size:12px;text-align:center;line-height:23px}
.copy{position:absolute;top:1162px;left:0;width:814px;height:38px;background:var(--footer-bottom);color:#fff;font-size:8.6px;line-height:38px;padding-left:81px}
</style>
</head>
<body>
<div class="page">
  <header>
    <div class="brand"><span class="brand-dot"></span><div><div class="brand-name">Corwin Hale Plumbing</div><div class="brand-tag">increasing energy efficiency by design</div></div></div>
    <div class="social header-social"><span></span><span></span><span></span><span></span></div>
    <div class="header-phone"><svg width="12" height="12" viewBox="0 0 24 24"><path fill="#6cbb3c" d="M6.6 10.8a15 15 0 006.6 6.6l2.2-2.2c.3-.3.7-.4 1-.2 1.1.4 2.3.6 3.6.6.6 0 1 .4 1 1V20c0 .6-.4 1-1 1A17 17 0 013 4c0-.6.4-1 1-1h3.5c.6 0 1 .4 1 1 0 1.3.2 2.5.6 3.6.1.3 0 .7-.2 1z"/></svg>TELEPHONE: <b>0412 586 204</b></div>
  </header>
  <nav class="nav"><a class="active">Home</a><a>Services</a><a>team</a><a>warrenty agent</a><a>contact us</a></nav>
  <div class="hero" role="img" aria-label="Commercial hot water units in a plant room"></div>
  <div class="dots"><i></i><i></i><i></i><i></i><i></i><i></i></div>

  <section class="card" style="left:90px"><h3>Services</h3><div class="photo" role="img" aria-label="Plumber fitting pipes under a sink" style="background:linear-gradient(135deg,#3d5c9a,#c7c9d0 60%,#b33)"></div><p>Our company is unique as we carry out work in all servicing areas including Solar Hot Water, Hydronic Heating, Warranty Agents, Roofing and Guttering, Fire Service in all the South West Area.</p><span class="btn">Learn More</span></section>
  <section class="card" style="left:309px"><h3>Team</h3><div class="photo" role="img" aria-label="Close-up of a steel sink drain" style="background:radial-gradient(circle,#333 18%,#aaa 26%,#f2f2f2 40%)"></div><p>Our company is unique as we carry out work in all servicing areas including Solar Hot Water, Hydronic Heating, Warranty Agents, Roofing and Guttering, Fire Service in all the South West Area.</p><span class="btn">Learn More</span></section>
  <section class="card" style="left:528px"><h3>Contact</h3><div class="photo" role="img" aria-label="Customer service staff wearing headsets" style="background:linear-gradient(90deg,#a8bfd8,#dfe6ee 60%,#c9a58f)"></div><p>Our company is unique as we carry out work in all servicing areas including Solar Hot Water, Hydronic Heating, Warranty Agents, Roofing and Guttering, Fire Service in all the South West Area.</p><span class="btn">Learn More</span></section>

  <section class="welcome">
    <h2>Welcome to CHP</h2>
    <p>Corwin Hale Plumbing Pty Ltd was established in 1986 and is known for high quality service that employs 5 qualified plumbing tradesmen, a Carpenter and a Sub Contractor working primarily in the Commercial and Industrial Sectors of Plumbing and Maintenance.</p>
    <p>As a locally owned Western Australian Industrial /Commercial/Maintenance Plumbing Company, we are committed to providing the best practice that will keep us as a leader in the competitive and challenging market of providing unique customer service to our clientele base.</p>
    <p>Committed to training we currently have 2 apprentice learning the trade under our direction to ensure our clientele have only the most up to date skills and techniques made available to each task at hand.</p>
    <p>We are members of The Regional Plumbers and Gas Fitters Guild and ensure work is carried out under the regulations of the 'Plumbers Licensing Board' using the Australian Standard AS3500 bylaws, contractors license number PL 4827.</p>
  </section>
  <div class="divider"></div>
  <section class="member">
    <h2>Member</h2>
    <svg class="badge" viewBox="0 0 175 200" role="img" aria-label="Trade association member badge"><circle cx="80" cy="70" r="62" fill="none" stroke="#4f9a27" stroke-width="4"/><circle cx="80" cy="70" r="34" fill="#6cbb3c"/><rect x="2" y="160" width="170" height="28" rx="3" fill="#4f9a27"/></svg>
  </section>

  <footer class="footer">
    <div class="col menu" style="left:81px"><h4>Main Menu</h4><a class="active">Home</a><a>Services</a><a>Team</a><a>Warrenty Agent</a><a>Contact</a></div>
    <div class="col" style="left:292px;width:180px">
      <h4>Contact Us</h4>
      <div class="contact-line"><svg width="11" height="11" viewBox="0 0 24 24"><path fill="#6cbb3c" d="M6.6 10.8a15 15 0 006.6 6.6l2.2-2.2c.3-.3.7-.4 1-.2 1.1.4 2.3.6 3.6.6.6 0 1 .4 1 1V20c0 .6-.4 1-1 1A17 17 0 013 4c0-.6.4-1 1-1h3.5c.6 0 1 .4 1 1 0 1.3.2 2.5.6 3.6.1.3 0 .7-.2 1z"/></svg><span><em>Telephone:</em> 0412 586 204</span></div>
      <div class="contact-line"><svg width="11" height="11" viewBox="0 0 24 24"><rect x="6" y="2" width="12" height="7" fill="#6cbb3c"/><rect x="2" y="10" width="20" height="10" fill="#6cbb3c"/></svg><span><em>FAX:</em> 08 9634 2817</span></div>
      <div class="contact-line"><svg width="11" height="11" viewBox="0 0 24 24"><rect x="1" y="5" width="22" height="14" fill="#6cbb3c"/><path d="M1 5l11 8 11-8" stroke="#5b5c5e" stroke-width="2" fill="none"/></svg><span><em>E-mail:</em> enquiries@corwinhaleplumb-<br><br>ing.com.au</span></div>
      <div class="social" style="margin-top:6px"><span></span><span></span><span></span><span></span></div>
    </div>
    <div class="col" style="left:576px"><h4>Get In Touch</h4><div class="field first">Name</div><div class="field">Email</div><div class="field area">Massege</div><div class="submit">Submit</div></div>
  </footer>
  <div class="copy">Copyright © Corwin Hale Plumbing 2011</div>
</div>
</body>
</html>
```